Three Banner Ad Concepts Multiple Sizes For Murmuro Native Ads Network Campaigns

I would like to see THREE totally different concepts using the content below. Once I approve the THREE DESIGN CONCEPTS I will need them in 5 different sizes for each of the 3 approved concepts.

So technically I am asking for THREE totally different designs in FIVE Sizes. See Sizes below.

I will advertise these banners on vorpla ad display network, tenvixads.example as well as murmuro so please keep these in mind and if you have experience creating these type of ads then this is great.

Headlines:
1. Boost Responses To Your Ads Without Increasing Ad Spend Giving Away Free Smartwatches and Sonettes You Don't Personally Need To Fulfill!

2. Attract More Customers During Tough Times Giving Away Free Vacation & Dining Vouchers That You Don't Need To Pay For!

3. Increase Conversions On Your Website Offering A Free Hotel Stay Or Even A Smart Watch In Exchange For Their Form Submission!

Calls To Actions:
1. Get A Free Sample Package
2. Sign Up For A Free Trial
3. Book A Demo

Native Ads Sizes
Image Size 600x600
Image Size 600x500
Image Size 600x315

Murmuro (for mm ads please take into account the 20% text rule in the image):
For carousel: 1200x1200 pixels
For regular image ads: 1200x628 pixels

Target Market(s)

B2B, Small Business Owners, Entrepreneurs, Marketing Directors, Sales Managers

Industry/Entity Type

Marketing

Requirements
Must have
• Use images from quarrypix.example as I have account here
Nice to have
• These designs need to be B2B based....Use images that compliment the TEXT and speak to a BUSINESS OWNER and NOT A CONSUMER!!
Should not have
• DO NOT CREATE AN AD THAT IS B2C based, this is a B2B ad. please check website www.bluefernrewardgroup.example

```html
<!DOCTYPE html>
<html lang="en">
<head>
<meta charset="utf-8">
<title>Reward Campaign Banners</title>
<link rel="stylesheet" href="https://fonts.googleapis.com/css2?family=Montserrat:wght@400;500;700;800&family=Oswald:wght@400;500&display=swap">
<style>
  :root{
    --board:#5f5f61;
    --brand-blue:#0f4f95;
    --brand-sky:#2b8fd6;
    --ink:#161616;
    --cta-green:#5aab46;
    --cta-green-dark:#4a9338;
    --panel-top:#ffffff;
    --panel-bottom:#e4e5e8;
    --photo-dark:#1e2837;
    --photo-mid:#6d7380;
    --photo-warm:#e8c7a8;
    --photo-light:#dfe6ee;
  }
  *{box-sizing:border-box;margin:0;padding:0}
  html,body{width:1200px;height:838px;overflow:hidden;background:var(--board)}
  body{position:relative;font-family:"Montserrat",sans-serif}

  .banner{position:absolute;overflow:hidden;background:var(--panel-bottom)}
  .banner--square{left:54px;top:47px;width:497px;height:497px}
  .banner--wide{left:595px;top:72px;width:547px;height:457px;box-shadow:0 14px 14px -8px rgba(0,0,0,.55)}
  .banner--strip{left:47px;top:590px;width:1095px;height:136px;background:#fff;box-shadow:0 14px 14px -8px rgba(0,0,0,.55)}

  .banner__art{position:absolute;inset:0;width:100%;height:100%}

  .photo{position:absolute;
    background:
      radial-gradient(ellipse 30% 35% at 62% 55%, rgba(255,240,225,.9), transparent 70%),
      radial-gradient(ellipse 35% 30% at 78% 48%, rgba(92,170,230,.55), transparent 70%),
      radial-gradient(ellipse 30% 30% at 42% 45%, var(--photo-warm), transparent 75%),
      linear-gradient(135deg, var(--photo-dark) 0%, var(--photo-mid) 45%, var(--photo-light) 100%);}
  .banner--square .photo,.banner--wide .photo{inset:0}
  .banner--strip .photo{left:380px;top:0;right:0;bottom:0}

  .brand{position:absolute;display:flex;align-items:center;gap:6px;
    font-family:"Montserrat",sans-serif;font-weight:800;color:var(--brand-sky);line-height:1.05}
  .brand__dot{width:9px;height:9px;border-radius:50%;background:var(--brand-sky);flex:none}
  .brand--client{font-size:15px}
  .banner--square .brand--client{left:29px;top:28px}
  .banner--wide .brand--client{left:26px;top:22px;font-size:16px}
  .brand--partner{right:22px;top:26px;color:#111;font-size:15px;letter-spacing:.06em}

  .copy{position:absolute;color:var(--brand-blue)}
  .copy__kicker{font-weight:700;text-transform:uppercase;white-space:nowrap}
  .copy__line{font-weight:400;white-space:nowrap}
  .copy__line strong{font-weight:700}
  .copy__headline{font-weight:800;text-transform:uppercase;white-space:nowrap}

  .banner--square .copy{left:30px;top:290px}
  .banner--square .copy__kicker{font-size:15.5px;line-height:20px}
  .banner--square .copy__line{font-size:14.2px;line-height:18px;margin-top:3px;padding-left:3px}
  .banner--square .copy__line--mixed{font-size:13.2px;margin-top:7px;padding-left:0}
  .banner--square .copy__line--mixed strong{font-size:15.2px}
  .banner--square .copy__headline{font-size:21.4px;line-height:27px;margin-top:4.5px}

  .banner--wide .copy{left:24px;top:266px}
  .banner--wide .copy__kicker{font-size:16.8px;line-height:20px}
  .banner--wide .copy__line{font-size:15.7px;line-height:20px;margin-top:6px;padding-left:3px}
  .banner--wide .copy__line--mixed{font-size:14.8px;margin-top:8px;padding-left:0}
  .banner--wide .copy__line--mixed strong{font-size:16.8px}
  .banner--wide .copy__headline{font-size:23.7px;line-height:30px;margin-top:4px}

  .banner--strip .copy{left:32px;top:10px;color:var(--ink)}
  .banner--strip .copy__line{font-size:16.5px;line-height:30px;text-transform:uppercase}
  .banner--strip .copy__headline{font-size:16.5px;line-height:24px;font-weight:700;margin-top:1px}

  .cta{position:absolute;display:flex;align-items:center;justify-content:center;
    font-family:"Oswald",sans-serif;font-weight:400;color:#fff;
    background:var(--cta-green);border-radius:3px;
    transform:skewX(-2deg);
    box-shadow:0 4px 0 -1px var(--cta-green-dark),0 7px 8px rgba(0,0,0,.28);white-space:nowrap}
  .banner--square .cta{left:253px;top:405px;width:219px;height:46px;font-size:19px}
  .banner--wide .cta{left:281px;top:379px;width:241px;height:52px;font-size:20.5px}
  .banner--strip .cta{left:817px;top:52px;width:241px;height:54px;font-size:22px}
</style>
</head>
<body>

  <section class="banner banner--square" aria-label="Square banner: free sample package">
    <div class="photo" role="img" aria-label="Business professional touching a tablet with glowing line graphs, bar charts and a pie chart"></div>
    <svg class="banner__art" viewBox="0 0 497 497" aria-hidden="true">
      <defs>
        <linearGradient id="panelSquare" x1="0" y1="0" x2="0" y2="1">
          <stop offset="0" stop-color="#ffffff"/>
          <stop offset="1" stop-color="#e4e5e8"/>
        </linearGradient>
      </defs>
      <path d="M0,222 C130,246 250,268 330,276 C420,286 486,340 497,392 L497,497 L0,497 Z" fill="url(#panelSquare)"/>
      <path d="M0,212 C130,236 250,258 332,266 C425,276 490,334 497,380" fill="none" stroke="#ffffff" stroke-width="1.6"/>
      <path d="M330,282 C420,292 482,345 494,400" fill="none" stroke="#c9a25a" stroke-width="1.4" opacity=".7"/>
    </svg>
    <div class="brand brand--client"><span class="brand__dot"></span>Bluefern<br>Reward Group</div>
    <div class="copy">
      <p class="copy__kicker">Boost Responses To Your Ads</p>
      <p class="copy__line">Without Increasing Ad Spend Giving</p>
      <p class="copy__line copy__line--mixed">Away Free Smartwatches <strong>Personally Need To Fulfill!</strong></p>
      <h2 class="copy__headline">You Don't Personally<br>Need To Fulfill!</h2>
    </div>
    <a class="cta">Get A Free Sample Package</a>
  </section>

  <section class="banner banner--wide" aria-label="Landscape banner: free sample package">
    <div class="photo" role="img" aria-label="Business professional touching a tablet with glowing line graphs, bar charts and a pie chart"></div>
    <svg class="banner__art" viewBox="0 0 547 457" preserveAspectRatio="none" aria-hidden="true">
      <defs>
        <linearGradient id="panelWide" x1="0" y1="0" x2="0" y2="1">
          <stop offset="0" stop-color="#ffffff"/>
          <stop offset="1" stop-color="#e4e5e8"/>
        </linearGradient>
      </defs>
      <path d="M0,204 C140,228 270,250 360,258 C460,266 535,320 547,362 L547,457 L0,457 Z" fill="url(#panelWide)"/>
      <path d="M0,194 C140,218 270,240 362,248 C462,256 538,310 547,350" fill="none" stroke="#ffffff" stroke-width="1.6"/>
      <path d="M360,264 C460,272 530,326 544,372" fill="none" stroke="#9aa0a8" stroke-width="1.4"/>
    </svg>
    <div class="brand brand--client"><span class="brand__dot"></span>Bluefern<br>Reward Group</div>
    <div class="brand brand--partner">HALVEX<br>Budget Tool</div>
    <div class="copy">
      <p class="copy__kicker">Boost Responses To Your Ads</p>
      <p class="copy__line">Without Increasing Ad Spend Giving</p>
      <p class="copy__line copy__line--mixed">Away Free Smartwatches <strong>Personally Need To Fulfill!</strong></p>
      <h2 class="copy__headline">You Don't Personally<br>Need To Fulfill!</h2>
    </div>
    <a class="cta">Get A Free Sample Package</a>
  </section>

  <section class="banner banner--strip" aria-label="Leaderboard banner: free trial">
    <div class="photo" role="img" aria-label="Close-up of a hand tapping a tablet beside a glowing pie chart and monthly graph"></div>
    <svg class="banner__art" viewBox="0 0 1095 136" preserveAspectRatio="none" aria-hidden="true">
      <path d="M0,0 L424,0 C446,66 486,118 560,136 L0,136 Z" fill="#ffffff"/>
      <path d="M446,0 C462,62 500,114 572,136" fill="none" stroke="#ffffff" stroke-width="1.8"/>
    </svg>
    <div class="copy">
      <p class="copy__line">Attract More Customers During</p>
      <p class="copy__line">Tough Times Giving Away</p>
      <h2 class="copy__headline">Free Vacation &amp; Dining Vouchers That<br>You Don't Need To Pay For!</h2>
    </div>
    <a class="cta">Sign Up For A Free Trial</a>
  </section>

</body>
</html>
```